South Carolina Bridal and Formal Wear Store

We want The Gown Parlor of Ashcombe website to feel luxurious, elegant, welcoming, and approachable—without feeling overpriced or intimidating. The site should immediately show that we are a full-service bridal and formal wear destination, offering bridal gowns, prom, mothers’ dresses, tuxedos and suits, accessories, and more. We want beautiful, high-end imagery and a clean, modern design while still reflecting the warm, personal experience customers receive when they walk into our boutique. Most importantly, the website should be easy to shop and navigate, allowing customers to browse our collections, see what we offer, understand price ranges, book appointments, and feel excited and comfortable choosing The Gown Parlor of Ashcombe for all of their special-event needs.

Target Market(s)

Women ages 18-50. Brides, engaged women, mothers of the occasion

Industry/Entity Type

Bridal and Formal Wear

Coding

Coded - Design and coding required

Number of Pages Required

5+ page

Font styles to use
Sans Serif

Colors

Designer to choose colors to be used in the design.

Requirements
Must have
• Appointment area, about us staff area, what we offer and designers our logo
Nice to have
• Modern Southern Luxury: Clean, elegant, and upscale with soft neutral tones, beautiful bridal photography, and a warm Lowcountry feel.
Should not have
• pricing

```html
<!DOCTYPE html>
<html lang="en">
<head>
<meta charset="utf-8">
<title>The Gown Parlor of Ashcombe</title>
<link rel="stylesheet" href="https://fonts.googleapis.com/css2?family=DM+Serif+Display&family=Montserrat:wght@400;500;600;700;800&display=swap">
<style>
:root{
  --ink:#111;
  --black:#000;
  --night:#141414;
  --footer:#1b1b1b;
  --cream:#fbf1e8;
  --mist:#f2f2f2;
  --tan:#d8b488;
  --white:#fff;
  --badge:#d2d2d2;
}
*{margin:0;padding:0;box-sizing:border-box}
html,body{width:1200px;height:3333px;overflow:hidden}
body{position:relative;background:var(--white);font-family:"Montserrat",sans-serif;color:var(--ink)}
.abs{position:absolute}
.serif{font-family:"DM Serif Display",serif;font-weight:400}
.center{text-align:center}
.photo{position:absolute}

/* hero */
.hero{left:0;top:0;width:1200px;height:451px;background:var(--black)}
.hero-photo{left:172px;top:0;width:914px;height:451px;
  background:
    radial-gradient(ellipse 60% 55% at 50% 40%,rgba(120,96,82,.55) 0%,rgba(60,48,42,.35) 50%,rgba(0,0,0,0) 80%),
    linear-gradient(180deg,#2a2826 0%,#1a1816 60%,#0d0c0b 100%)}
.brand{font-weight:600;color:var(--white);font-size:14px;letter-spacing:.3px;line-height:1.15;display:flex;align-items:center;gap:8px}
.brand .dot{width:10px;height:10px;border-radius:50%;background:var(--tan);flex:none}
.hero .brand{left:117px;top:24px;width:190px}
.nav{left:309px;top:36px;display:flex;gap:12px;font-size:10.5px;font-weight:500;color:var(--white);text-transform:uppercase}
.btn-tan{background:var(--tan);color:#1a1a1a;font-size:10.5px;font-weight:500;text-transform:uppercase;display:flex;align-items:center;justify-content:center}
.hero .btn-tan{left:923px;top:31px;width:158px;height:23px}
.hero h1{left:172px;width:914px;top:166px;color:var(--white);font-size:56px;line-height:50px;letter-spacing:1px}
.hero p{left:285px;width:630px;top:290px;color:var(--white);font-size:11.5px;line-height:15px}
.btn-line{display:flex;align-items:center;justify-content:center;font-size:11px;border:1.5px solid currentColor;border-radius:3px}
.hero .btn-line{left:495px;top:356px;width:181px;height:25px;color:var(--white)}

/* about */
.about h2{left:0;width:1200px;top:485px;font-size:50px;line-height:49px;letter-spacing:1px}
.about-photo{left:172px;top:637px;width:306px;height:359px;
  background:
    radial-gradient(ellipse 45% 55% at 52% 70%,#efe8db 0%,#ddd2bf 45%,rgba(200,185,160,0) 75%),
    linear-gradient(180deg,#7a6446 0%,#a48c67 35%,#b7a584 60%,#8a7558 100%)}
.about .lead{left:548px;top:692px;width:440px;font-size:17.5px;line-height:22.5px}
.about .body{left:548px;top:816px;width:440px;font-size:12px;line-height:16.5px;font-weight:500}
.about .btn-line{left:548px;top:909px;width:114px;height:28px;color:var(--ink)}

/* milestones */
.milestones{left:0;top:1045px;width:1200px;height:481px;background:var(--cream)}
.milestones h2{left:116px;top:30px;font-size:44px;line-height:44px;letter-spacing:1px}
.cards{left:5px;top:149px;display:flex;gap:5px}
.card{width:234px}
.card .pic{height:186px}
.card h3{font-family:"DM Serif Display",serif;font-weight:400;font-size:17px;line-height:17px;margin:15px 0 0 7px;width:160px;height:38px;letter-spacing:.3px}
.card p{font-size:9.5px;line-height:13px;font-weight:500;margin:4px 7px 0}

/* partners */
.partners h2{left:0;width:1200px;top:1565px;font-size:50px;line-height:49px;letter-spacing:1px}
.partners .sub{left:0;width:1200px;top:1682px;font-size:17px;font-weight:500}
.partners .small{left:0;width:1200px;top:1710px;font-size:12px;line-height:16px}
.badges{left:75px;top:1774px;width:1010px;display:flex;justify-content:space-between;align-items:center}
.badge{width:104px;height:34px;background:var(--badge);border-radius:4px}
.badge.round{width:48px;height:34px;border-radius:50%}

/* team */
.team{left:0;top:1869px;width:1200px;height:232px;background:var(--mist)}
.team h2{left:0;width:1200px;top:42px;font-size:50px;line-height:49px;letter-spacing:1px}
.team p{left:240px;width:720px;top:162px;font-size:12.5px;line-height:16px}
.staff{left:0;top:2101px;width:1200px;height:214px;display:flex;gap:2px}
.staff div{flex:1}

/* testimonials */
.eyebrow{left:0;width:1200px;top:2350px;font-size:11px;font-weight:700;letter-spacing:.3px}
.reviews h2{left:0;width:1200px;top:2386px;font-size:50px;line-height:47px;letter-spacing:1px}
.quote{top:2540px;width:300px;font-size:13px;line-height:17px}
.quote strong{display:block;margin-top:8px;font-size:14px;font-weight:700}
.arrow{top:2567px}
.reviews .btn-line{left:534px;top:2653px;width:175px;height:28px;color:var(--ink)}

/* cta */
.cta{left:0;top:2729px;width:1200px;height:297px;background:var(--night)}
.cta-photo{left:560px;top:0;width:640px;height:297px;
  background:
    radial-gradient(ellipse 30% 60% at 30% 55%,rgba(210,196,180,.35) 0%,rgba(90,78,70,.25) 50%,rgba(0,0,0,0) 80%),
    linear-gradient(90deg,#141414 0%,#2a2421 35%,#1e1b19 100%)}
.cta h2{left:100px;top:60px;font-size:42px;line-height:42px;color:var(--white);letter-spacing:1px}
.cta p{left:103px;top:168px;width:440px;font-size:13px;line-height:14px;color:var(--white)}
.cta .btn-tan{left:103px;top:218px;width:159px;height:24px}

/* footer */
.footer{left:0;top:3026px;width:1200px;height:307px;background:var(--footer);color:var(--white)}
.footer .brand{left:107px;top:54px;width:175px}
.socials{left:150px;top:106px;display:flex;gap:8px}
.socials span{width:28px;height:28px;border:2px solid var(--white);border-radius:50%}
.f-head{font-size:11px;font-weight:600;text-transform:uppercase}
.f-links{font-size:10.5px;line-height:15.5px}
.f-sub{left:681px;top:54px;width:170px;font-size:10px;line-height:12px}
.footer .btn-tan{left:681px;top:92px;width:162px;height:24px;font-size:11px}
.contact{left:904px;display:flex;align-items:center;gap:15px;font-size:12.5px}
.contact svg{flex:none}
.copy{left:0;width:1208px;top:160px;font-size:10.5px}
.wordmark{left:0;top:212px;width:1200px;height:95px;background:var(--black);overflow:hidden}
.wordmark span{position:absolute;left:0;width:1200px;text-align:center;top:6px;font-weight:800;font-size:126px;line-height:126px;color:var(--white);letter-spacing:2px;white-space:nowrap}
</style>
</head>
<body>

<section class="abs hero">
  <div class="photo hero-photo" role="img" aria-label="Boutique stylists posing together in front of racks of gowns"></div>
  <div class="abs brand"><span class="dot"></span>The Gown Parlor of Ashcombe</div>
  <nav class="abs nav"><span>Bridal</span><span>Prom &amp; Special Occasion</span><span>Mothers &amp; Guests</span><span>Tuxedos &amp; Suits</span><span>Accessories</span><span>Designers</span></nav>
  <div class="abs btn-tan">Book an Appointment</div>
  <h1 class="abs serif center">Where Every Ashcombe<br>Story Begins.</h1>
  <p class="abs center">The Gown Parlor Of Ashcombe Is The Lowcountry's Destination For Bridal Gowns, Tuxedos, Prom, And Formalwear — Curated With Care, Fitted With Love, And Styled For Every Milestone In Your Story.</p>
  <div class="abs btn-line">BOOK YOUR APPOINTMENT</div>
</section>

<section class="about">
  <h2 class="abs serif center">More Than a Boutique<br>— An Ashcombe Tradition.</h2>
  <div class="photo about-photo" role="img" aria-label="Bride in a strapless ivory ball gown standing in an ornate gilded room"></div>
  <p class="abs lead">Nestled In The Heart Of The Lowcountry, The Gown Parlor Of Ashcombe Has Helped Generations Of Brides, Grooms, And Their Families Feel Confident, Celebrated, And Beautiful For Life's Biggest Moments.</p>
  <p class="abs body">Nestled in the heart of the Lowcountry, The Gown Parlor of Ashcombe has helped generations of brides, grooms, and their families feel confident, celebrated, and beautiful for life's biggest moments.</p>
  <div class="abs btn-line">Read More</div>
</section>

<section class="abs milestones">
  <h2 class="abs serif">Every Milestone Deserves the<br>Perfect Fit.</h2>
  <div class="abs cards">
    <article class="card"><div class="pic" role="img" aria-label="Smiling woman in an elegant black dress" style="background:radial-gradient(ellipse 50% 60% at 50% 40%,#b08d78 0%,#5a463c 45%,rgba(0,0,0,0) 80%),linear-gradient(180deg,#8c8e92,#2a2624 75%,#1a1716)"></div><h3>Mothers' &amp; Guest Dresses</h3><p>Elegance for the Whole Family." Sophisticated pieces so every mother feels just as radiant.</p></article>
    <article class="card"><div class="pic" role="img" aria-label="Bride in a strapless ball gown beside a piano" style="background:radial-gradient(ellipse 40% 60% at 58% 70%,#f2ede5 0%,#ddd3c4 45%,rgba(0,0,0,0) 80%),linear-gradient(180deg,#e8dfcf,#b59c78 55%,#6e5438)"></div><h3>Bridal Gowns</h3><p>Say Yes, Ashcombe Style." Designer gowns from classic Lowcountry romance to modern silhouettes.</p></article>
    <article class="card"><div class="pic" role="img" aria-label="Couple embracing in a blush tulle gown in a garden" style="background:radial-gradient(ellipse 55% 45% at 45% 78%,#f1d2c8 0%,#dcb1a4 45%,rgba(0,0,0,0) 80%),linear-gradient(180deg,#8a9a76,#6a6a58 45%,#b9958a)"></div><h3>Prom &amp; Special Occasion</h3><p>Your Night, Your Statement." Bold, on-trend styles for the moment everyone remembers.</p></article>
    <article class="card"><div class="pic" role="img" aria-label="Groom in a navy tuxedo with bow tie" style="background:radial-gradient(ellipse 40% 55% at 50% 70%,#2f3c52 0%,#1f2836 55%,rgba(0,0,0,0) 85%),linear-gradient(180deg,#6b5640,#3a2e26 55%,#1a1816)"></div><h3>Tuxedos &amp; Suits</h3><p>Sharp. Classic. Unmistakably You." Full tuxedo and suit rentals and purchases for grooms and groomsmen.</p></article>
    <article class="card"><div class="pic" role="img" aria-label="Close view of a woman wearing a jeweled drop earring" style="background:radial-gradient(ellipse 50% 60% at 40% 45%,#d9b79a 0%,#a5795c 45%,rgba(0,0,0,0) 85%),linear-gradient(135deg,#cdb59c,#5a3f30 70%,#2a1e18)"></div><h3>Accessories</h3><p>The Final Touch." Veils, jewelry, belts, shoes, and cufflinks to complete every look.</p></article>
  </div>
</section>

<section class="partners">
  <h2 class="abs serif center">Curated From the Best,<br>Fit for You.</h2>
  <p class="abs sub center">We hand-select every collection we carry — from timeless bridal</p>
  <p class="abs small center">houses to the freshest prom and formalwear labels — so you always have beautiful,<br>current options waiting when you walk through our doors.</p>
  <div class="abs badges">
    <span class="badge"></span><span class="badge"></span><span class="badge round"></span><span class="badge"></span><span class="badge"></span><span class="badge"></span><span class="badge"></span>
  </div>
</section>

<section class="abs team">
  <h2 class="abs serif center">The Friendly Faces Behind<br>Every Fitting</h2>
  <p class="abs center">Our stylists aren't just here to sell a dress or suit — we're here to listen, guide, and celebrate with you. Get to know the team who will make your appointment feel like time with family.</p>
</section>
<div class="abs staff">
  <div role="img" aria-label="Portrait of a stylist with wavy brown hair" style="background:radial-gradient(ellipse 35% 60% at 50% 50%,#c9a088 0%,#7a5a48 45%,rgba(0,0,0,0) 80%),linear-gradient(180deg,#4a4644,#2a2624)"></div>
  <div role="img" aria-label="Portrait of a smiling young stylist" style="background:radial-gradient(ellipse 35% 60% at 50% 50%,#d4aa92 0%,#6e4a36 45%,rgba(0,0,0,0) 80%),linear-gradient(180deg,#4c4846,#2a2624)"></div>
  <div role="img" aria-label="Portrait of a stylist wearing glasses" style="background:radial-gradient(ellipse 35% 60% at 50% 50%,#d8b39c 0%,#5a3e30 45%,rgba(0,0,0,0) 80%),linear-gradient(180deg,#4a4644,#2a2624)"></div>
  <div role="img" aria-label="Portrait of a stylist with long dark hair" style="background:radial-gradient(ellipse 35% 60% at 50% 50%,#cfa48c 0%,#3e2e26 45%,rgba(0,0,0,0) 80%),linear-gradient(180deg,#4c4846,#2a2624)"></div>
</div>

<section class="reviews">
  <p class="abs eyebrow center">REAL BRIDES, REAL GROOMS</p>
  <h2 class="abs serif center">Love, As Told By Our<br>Ashcombe Families.</h2>
  <svg class="abs arrow" style="left:108px" width="12" height="16" viewBox="0 0 12 16"><path d="M9 2 3 8l6 6" fill="none" stroke="#111" stroke-width="1.5"/></svg>
  <div class="abs quote" style="left:146px">"They made me feel like the most important bride in the room — from the first fitting to the final steal." —<strong>Claire Hollis</strong></div>
  <div class="abs quote" style="left:480px">"Found the perfect tux for my son's prom in one visit — no stress, just great style."<strong>Daniel Pruitt</strong></div>
  <div class="abs quote" style="left:795px">"My mother-of-the-bride dress was stunning, and the staff treated me like family the whole time."<strong>Margaret Lyle</strong></div>
  <svg class="abs arrow" style="left:1114px" width="12" height="16" viewBox="0 0 12 16"><path d="m3 2 6 6-6 6" fill="none" stroke="#111" stroke-width="1.5"/></svg>
  <div class="abs btn-line">View all Testimonials</div>
</section>

<section class="abs cta">
  <div class="photo cta-photo" role="img" aria-label="Bride in a veil holding a bouquet, shown in profile"></div>
  <h2 class="abs serif">Come See Us in the<br>Heart of Ashcombe.</h2>
  <p class="abs">Step inside and experience Lowcountry hospitality with every fitting. We can't wait to meet you.</p>
  <div class="abs btn-tan">Book an Appointment</div>
</section>

<footer class="abs footer">
  <div class="abs brand"><span class="dot"></span>The Gown Parlor of Ashcombe</div>
  <div class="abs socials"><span></span><span></span><span></span></div>
  <p class="abs f-head" style="left:314px;top:28px">Quick Links</p>
  <div class="abs f-links" style="left:314px;top:56px">Home<br>Bridal<br>Prom &amp; Special Occasion<br>Mothers &amp; Guests<br>Tuxedos &amp; Suits</div>
  <div class="abs f-links" style="left:503px;top:58px">Accessories<br>Designers<br>About Us<br>Book an Appointment<br>Contact</div>
  <p class="abs f-head" style="left:684px;top:28px">Subscribe Newsletter</p>
  <p class="abs f-sub">Get Latest updates via email directly in your inbox</p>
  <div class="abs btn-tan">Subscribe Now</div>
  <p class="abs f-head" style="left:935px;top:28px">Contact Us</p>
  <div class="abs contact" style="top:56px"><svg width="26" height="26" viewBox="0 0 26 26"><circle cx="13" cy="13" r="12" fill="none" stroke="#fff" stroke-width="1.3"/><path d="M9 8c0 5 4 9 9 9l1-2-2-1.5-1.5 1c-1.5-.7-2.8-2-3.5-3.5l1-1.5L11.5 7z" fill="#fff"/></svg><strong>555-014-2290</strong></div>
  <div class="abs contact" style="top:88px"><svg width="26" height="26" viewBox="0 0 26 26"><circle cx="13" cy="13" r="12" fill="none" stroke="#fff" stroke-width="1.3"/><rect x="7.5" y="9" width="11" height="8" fill="none" stroke="#fff" stroke-width="1.3"/><path d="m7.5 9 5.5 4.5L18.5 9" fill="none" stroke="#fff" stroke-width="1.3"/></svg><span style="text-decoration:underline">hello@gownparlorashcombe.com</span></div>
  <div class="abs contact" style="top:120px;align-items:flex-start"><svg width="26" height="26" viewBox="0 0 26 26"><circle cx="13" cy="13" r="12" fill="none" stroke="#fff" stroke-width="1.3"/><path d="M13 6a4.5 4.5 0 0 0-4.5 4.5C8.5 14 13 19 13 19s4.5-5 4.5-8.5A4.5 4.5 0 0 0 13 6zm0 6.2a1.7 1.7 0 1 1 0-3.4 1.7 1.7 0 0 1 0 3.4z" fill="#fff"/></svg><span style="line-height:17px">418 Magnolia Bend Rd.<br>Ashcombe, SC 29900, USA</span></div>
  <p class="abs copy center">Copyright © 2026 The Gown Parlor of Ashcombe</p>
  <div class="abs wordmark"><span>GOWN PARLOR</span></div>
</footer>

</body>
</html>
```